Label Design for Saffron Company

We need a label design that is unique for our container. The item inside the container is Saffron, and it is 5g in weigh. We need on the label our logo, the weight and quality. Here is the exactly what we want. We want the background to be black for the label and the design to present royalty, and premium quality.

Premium Quality
Grade A+ Premium Saffron
100% Natural and Pure
www.VelmoraSpice.com

Target Market(s)

Everyone

Requirements
Must have
• Black background, golden border design. Unique design, that show premium and royalty.
Nice to have
• The logo is attached with transparent background so you can show exactly how things look like.
Should not have
• different colors that are not part of the logo.

```html
<!DOCTYPE html>
<html lang="en">
<head>
<meta charset="utf-8">
<title>Velmora Spice – Saffron Tin Label</title>
<link rel="stylesheet" href="https://fonts.googleapis.com/css2?family=Cinzel:wght@400&family=Montserrat:wght@600;700&display=swap">
<style>
  :root {
    --paper: #ffffff;
    --label-black: #1f1c1c;
    --gold: #d9b25c;
    --gold-light: #f3dc97;
    --gold-deep: #a87a2a;
    --wordmark: #f4f1ea;
    --grey-text: #d9d6d2;
    --weight-red: #e31b23;
  }
  html, body {
    margin: 0;
    padding: 0;
    width: 900px;
    height: 1200px;
    overflow: hidden;
    background: var(--paper);
  }
  .canvas {
    width: 900px;
    height: 1200px;
    display: block;
  }
  .label-disc { fill: var(--label-black); }
  .inner-rule { fill: none; stroke: var(--gold); stroke-width: 2; }
  .quality-arc {
    font-family: "Montserrat", sans-serif;
    font-weight: 600;
    font-size: 24px;
    letter-spacing: 1px;
    fill: var(--gold);
  }
  .grade-arc {
    font-family: "Montserrat", sans-serif;
    font-weight: 700;
    font-size: 26px;
    fill: var(--grey-text);
  }
  .brand-mark { fill: none; stroke: var(--gold); stroke-width: 3; }
  .brand-name {
    font-family: "Cinzel", serif;
    font-weight: 400;
    fill: var(--wordmark);
    text-anchor: middle;
  }
  .brand-top { font-size: 36px; letter-spacing: 6px; }
  .brand-bottom { font-size: 56px; letter-spacing: 1px; }
  .claim-rule { stroke: var(--gold); stroke-width: 1.5; }
  .claim-text {
    font-family: "Montserrat", sans-serif;
    font-weight: 600;
    font-size: 23px;
    fill: var(--gold);
    text-anchor: middle;
  }
  .weight-badge { fill: var(--weight-red); }
  .weight-value {
    font-family: "Montserrat", sans-serif;
    font-weight: 700;
    font-size: 22px;
    fill: #ffffff;
  }
  .weight-unit {
    font-family: "Montserrat", sans-serif;
    font-weight: 700;
    font-size: 12px;
    fill: #ffffff;
  }
</style>
</head>
<body>
<svg class="canvas" viewBox="0 0 900 1200" xmlns="http://www.w3.org/2000/svg">
  <defs>
    <linearGradient id="gold-wash" x1="0" y1="0" x2="1" y2="1">
      <stop offset="0" stop-color="var(--gold-light)"/>
      <stop offset="0.5" stop-color="var(--gold)"/>
      <stop offset="1" stop-color="var(--gold-deep)"/>
    </linearGradient>
    <path id="top-arc" d="M 194 600 A 256 256 0 0 1 706 600"/>
    <path id="bottom-arc" d="M 179 600 A 271 271 0 0 0 721 600"/>
  </defs>

  <g class="label">
    <circle class="label-disc" cx="450" cy="600" r="362"/>

    <path class="wreath-border" role="img" aria-label="Golden laurel wreath border around the label"
          fill="url(#gold-wash)" fill-rule="evenodd" opacity="0.85"
          d="M 450 249 A 351 351 0 1 1 449.9 249 Z M 450 285 A 315 315 0 1 0 450.1 285 Z"/>

    <circle class="inner-rule" cx="450" cy="600" r="307"/>

    <text class="quality-arc">
      <textPath href="#top-arc" startOffset="50%" text-anchor="middle">PREMIUM QUALITY</textPath>
    </text>

    <g class="brand">
      <rect class="brand-mark" x="382" y="383" width="136" height="136" rx="14"/>
      <text class="brand-name brand-top" x="450" y="580">VELMORA</text>
      <text class="brand-name brand-bottom" x="450" y="636">SPICE</text>
    </g>

    <g class="claim">
      <line class="claim-rule" x1="300" y1="675" x2="600" y2="675"/>
      <text class="claim-text" x="450" y="702">100% Natural and Pure</text>
      <line class="claim-rule" x1="300" y1="713" x2="600" y2="713"/>
    </g>

    <g class="weight">
      <circle class="weight-badge" cx="450" cy="799" r="26"/>
      <text x="450" y="807" text-anchor="middle"><tspan class="weight-value">5</tspan><tspan class="weight-unit" dx="2">gr</tspan></text>
    </g>

    <text class="grade-arc">
      <textPath href="#bottom-arc" startOffset="50%" text-anchor="middle">Grade A+ Premium Saffron</textPath>
    </text>
  </g>
</svg>
</body>
</html>
```